New Business Card Design Project

Want a simple but attention grabbing business card. Back Side having mainly our logo and basic info-the front side a typical business card.

Contact Information for Business Card

Hearth & Tile Interiors
218 NW Larkspur Rd. Suite 207
Ankeny, Iowa 50021

phone- 515.482.7093

website is -htidesigns.com

```html
<!DOCTYPE html>
<html lang="en">
<head>
<meta charset="utf-8">
<title>Hearth &amp; Tile Interiors — Business Card</title>
<link href="https://fonts.googleapis.com/css2?family=Montserrat:wght@600;700;800&family=Open+Sans:wght@400;600&display=swap" rel="stylesheet">
<style>
  :root {
    --navy: #0c1628;
    --blue: #2370bd;
    --orange: #ea5b25;
    --white: #ffffff;
    --ink: #1d1d1f;
    --backdrop: #2a2b2e;
  }
  * { margin: 0; padding: 0; box-sizing: border-box; }
  html, body { width: 1200px; height: 780px; overflow: hidden; }
  body {
    background: var(--backdrop);
    position: relative;
    font-family: "Open Sans", sans-serif;
  }
  .card {
    position: absolute;
    width: 560px;
    height: 320px;
    border-radius: 26px;
    overflow: hidden;
    box-shadow: 0 14px 30px rgba(0,0,0,.45);
  }
  .card-bg { position: absolute; inset: 0; width: 100%; height: 100%; }
  .card--brand { left: 50px; top: 60px; background: var(--navy); }
  .card--contact { left: 590px; top: 400px; background: var(--white); }

  .wordmark {
    position: absolute;
    display: flex;
    align-items: center;
    gap: 12px;
    font-family: "Montserrat", sans-serif;
    font-weight: 800;
    color: var(--orange);
    text-transform: uppercase;
    line-height: 1.05;
  }
  .wordmark-square {
    background: var(--orange);
    flex: none;
  }
  .card--brand .wordmark { left: 200px; top: 152px; font-size: 30px; letter-spacing: 1px; }
  .card--brand .wordmark-square { width: 22px; height: 22px; }
  .card--contact .wordmark { left: 26px; top: 34px; font-size: 14px; letter-spacing: .5px; gap: 7px; }
  .card--contact .wordmark-square { width: 11px; height: 11px; }

  .person {
    position: absolute;
    left: 36px;
    bottom: 40px;
  }
  .person-name {
    font-family: "Montserrat", sans-serif;
    font-weight: 800;
    font-size: 26px;
    color: var(--orange);
    text-transform: uppercase;
  }
  .person-name .first { color: var(--blue); }
  .person-title {
    margin-top: 2px;
    font-family: "Montserrat", sans-serif;
    font-weight: 600;
    font-size: 11px;
    letter-spacing: 4px;
    color: var(--ink);
    text-transform: uppercase;
  }

  .contact-list {
    position: absolute;
    left: 310px;
    top: 150px;
    list-style: none;
    font-size: 13px;
    font-weight: 600;
    color: var(--ink);
  }
  .contact-item {
    display: flex;
    align-items: flex-start;
    gap: 10px;
    margin-bottom: 10px;
    line-height: 1.3;
  }
  .contact-icon { width: 15px; height: 15px; flex: none; margin-top: 1px; }
</style>
</head>
<body>

  <section class="card card--brand" aria-label="Card back: brand side">
    <svg class="card-bg" viewBox="0 0 560 320" preserveAspectRatio="none" aria-hidden="true">
      <polygon points="0,0 560,0 560,62 220,104 0,268" fill="var(--orange)"/>
      <polygon points="0,268 220,104 560,62 560,78 248,128 0,286" fill="var(--blue)"/>
    </svg>
    <div class="wordmark">
      <span class="wordmark-square"></span>
      <span>Hearth &amp; Tile<br>Interiors</span>
    </div>
  </section>

  <section class="card card--contact" aria-label="Card front: contact side">
    <svg class="card-bg" viewBox="0 0 560 320" preserveAspectRatio="none" aria-hidden="true">
      <polygon points="0,0 560,0 560,70 350,100 0,200" fill="var(--navy)"/>
      <polygon points="0,200 350,100 560,70 560,90 375,122 0,218" fill="var(--blue)"/>
    </svg>

    <div class="wordmark">
      <span class="wordmark-square"></span>
      <span>Hearth &amp; Tile<br>Interiors</span>
    </div>

    <ul class="contact-list">
      <li class="contact-item">
        <svg class="contact-icon" viewBox="0 0 24 24" aria-hidden="true"><path fill="var(--orange)" d="M6.6 10.8a15.5 15.5 0 0 0 6.6 6.6l2.2-2.2a1 1 0 0 1 1-.25 11.4 11.4 0 0 0 3.6.57 1 1 0 0 1 1 1V20a1 1 0 0 1-1 1A17 17 0 0 1 3 4a1 1 0 0 1 1-1h3.5a1 1 0 0 1 1 1c0 1.250.2 2.450.57 3.6a1 1 0 0 1-.25 1z"/></svg>
        <span>515.482.7093</span>
      </li>
      <li class="contact-item">
        <svg class="contact-icon" viewBox="0 0 24 24" aria-hidden="true"><rect x="2" y="5" width="20" height="14" rx="1" fill="var(--orange)"/><path d="M2.5 6l9.5 7 9.5-7" fill="none" stroke="var(--white)" stroke-width="1.6"/></svg>
        <span>hello@htidesigns.com</span>
      </li>
      <li class="contact-item">
        <svg class="contact-icon" viewBox="0 0 24 24" aria-hidden="true"><path fill="var(--orange)" d="M12 2a7 7 0 0 0-7 7c0 5.2 7 13 7 13s7-7.8 7-13a7 7 0 0 0-7-7zm0 9.5A2.5 2.5 0 1 1 12 6.5a2.5 2.5 0 0 1 0 5z"/></svg>
        <span>218 NW Larkspur Rd. Suite 207<br>Ankeny, Iowa 50021</span>
      </li>
      <li class="contact-item">
        <svg class="contact-icon" viewBox="0 0 24 24" aria-hidden="true"><circle cx="12" cy="12" r="9.5" fill="none" stroke="var(--orange)" stroke-width="2"/><path d="M2.5 12h19M12 2.5c3 3 3 16 0 19M12 2.5c-3 3-3 16 0 19" fill="none" stroke="var(--orange)" stroke-width="1.6"/></svg>
        <span>htidesigns.com</span>
      </li>
    </ul>

    <div class="person">
      <div class="person-name"><span class="first">Your</span> Namehere</div>
      <div class="person-title">Designation</div>
    </div>
  </section>

</body>
</html>
```